BrickaFun Business Card

We need a business card design for our company. We sell construction-themed amusement rides for kids.

Contact Information for Business Card

Contact info on business card should include:
Dale Hurst
Co-Founder & COO
(833) 517-BRICKAF
Dale@brickafun.com
www.brickafun.com

```html
<!DOCTYPE html>
<html lang="en">
<head>
<meta charset="utf-8">
<title>BrickaFun Business Card</title>
<link href="https://fonts.googleapis.com/css2?family=Roboto:wght@400;500;700&display=swap" rel="stylesheet">
<style>
  :root {
    --bg: #e6e6e6;
    --card: #050505;
    --edge: #f07a22;
    --orange: #f08a2c;
    --text: #e8e8e8;
    --muted: #bdbdbd;
    --rule: #6a6a6a;
    --art-a: #f2c21a;
    --art-b: #e8602c;
    --art-c: #2f4f8f;
  }
  * { margin: 0; padding: 0; box-sizing: border-box; }
  html, body { width: 1200px; height: 801px; overflow: hidden; }
  body {
    background: var(--bg);
    font-family: "Roboto", Arial, sans-serif;
    display: flex;
    align-items: center;
    justify-content: center;
    gap: 36px;
  }
  .card {
    position: relative;
    width: 550px;
    height: 314px;
    background: var(--card);
    border-bottom: 3px solid var(--edge);
    border-left: 2px solid var(--edge);
    box-shadow: 0 10px 24px rgba(0,0,0,.18);
    overflow: hidden;
  }
  .brand-name {
    position: absolute;
    color: var(--orange);
    font-weight: 700;
    letter-spacing: -0.5px;
    line-height: 1;
  }
  /* contact side */
  .card--contact .brand-name { top: 42px; right: 40px; font-size: 40px; }
  .card--contact .top-rule {
    position: absolute; top: 102px; right: 0; width: 230px; height: 1px; background: var(--rule);
  }
  .person { position: absolute; left: 40px; top: 170px; }
  .person__name { color: var(--orange); font-size: 22px; font-weight: 500; }
  .person__role { color: var(--text); font-size: 14px; margin-top: 4px; }
  .card--contact .mid-rule {
    position: absolute; left: 40px; right: 0; top: 226px; height: 1px; background: var(--rule);
  }
  .contact-list { position: absolute; left: 40px; top: 236px; list-style: none; }
  .contact-list li {
    display: flex; align-items: center; gap: 10px;
    color: var(--text); font-size: 14px; line-height: 22px;
  }
  .contact-list svg { width: 13px; height: 13px; fill: var(--orange); flex: none; }
  .contact-list .accent { color: var(--orange); }
  /* brand side */
  .crew-art {
    position: absolute; left: 20px; bottom: 0; width: 260px; height: 270px;
    background: linear-gradient(160deg, var(--art-a) 0%, var(--art-b) 50%, var(--art-c) 100%);
    opacity: .85; border-radius: 8px 8px 0 0;
  }
  .card--brand .brand-name { top: 132px; right: 44px; font-size: 48px; }
</style>
</head>
<body>
  <section class="card card--contact">
    <div class="brand-name">BrickaFun</div>
    <div class="top-rule"></div>
    <div class="person">
      <div class="person__name">Dale Hurst</div>
      <div class="person__role">Co-Founder &amp; COO</div>
    </div>
    <div class="mid-rule"></div>
    <ul class="contact-list">
      <li>
        <svg viewBox="0 0 24 24" aria-hidden="true"><path d="M6.6 10.8a15.1 15.1 0 0 0 6.6 6.6l2.2-2.2a1 1 0 0 1 1-.25 11.4 11.4 0 0 0 3.6.57 1 1 0 0 1 1 1V20a1 1 0 0 1-1 1A17 17 0 0 1 3 4a1 1 0 0 1 1-1h3.5a1 1 0 0 1 1 1c0 1.25.2 2.45.57 3.57a1 1 0 0 1-.25 1z"/></svg>
        (833) 517-BRICKAF
      </li>
      <li>
        <svg viewBox="0 0 24 24" aria-hidden="true"><path d="M2 5h20v14H2zm2 2v.5l8 5 8-5V7zm0 2.8V17h16V9.8l-8 5z"/></svg>
        Dale@brickafun.com
      </li>
      <li>
        <svg viewBox="0 0 24 24" aria-hidden="true"><path d="M12 2a10 10 0 1 0 0 20 10 10 0 0 0 0-20zm6.9 6h-3a15.6 15.6 0 0 0-1.4-3.6A8 8 0 0 1 18.9 8zM12 4c.8 1.2 1.5 2.5 1.9 4h-3.8c.4-1.5 1.1-2.8 1.9-4zM4.3 14a8.2 8.2 0 0 1 0-4h3.4a16.5 16.5 0 0 0 0 4zm.8 2h3a15.6 15.6 0 0 0 1.4 3.6A8 8 0 0 1 5.1 16zm3-8h-3a8 8 0 0 1 4.4-3.6A15.6 15.6 0 0 0 8.1 8zM12 20c-.8-1.2-1.5-2.5-1.9-4h3.8c-.4 1.5-1.1 2.8-1.9 4zm2.3-6H9.7a14.7 14.7 0 0 1 0-4h4.6a14.7 14.7 0 0 1 0 4zm.2 5.6a15.6 15.6 0 0 0 1.4-3.6h3a8 8 0 0 1-4.4 3.6zm1.8-5.6a16.5 16.5 0 0 0 0-4h3.4a8.2 8.2 0 0 1 0 4z"/></svg>
        <span>www.<span class="accent">brickafun</span>.com</span>
      </li>
    </ul>
  </section>

  <section class="card card--brand">
    <div class="crew-art" role="img" aria-label="Cartoon illustration of two construction workers in hard hats and safety vests"></div>
    <div class="brand-name">BrickaFun</div>
  </section>
</body>
</html>
```